Cobalt Field Services website design

We want to create a Sports turf website for our business Cobalt Field Services - we do sports turf management on sports fields around the Mackay region soccer rugby league softball fields etc from full turf management plans and maintenance to just supply and apply of turf management products and just supply of products with program we also do grounds facility maintenance at council facility's and grounds that require a higher level of care - we will up load our logos and fonts etc to assist with the colour pallet for the website - we will have to have a landing page a shop page with tabs a gallery tab along with a grants initiative and our northreach finest green tab also - our font for the txt is called ethnocentric
Updates

how do we open time for people to submit we have no one submitted

Industry/Entity Type

Turf

Coding

Coded - Design and coding required

Number of Pages Required

5+ page

Font styles to use
Other font styles liked:
• ethnocentric

Requirements
Must have
• I have mentioned some waffle in the description that should assist
Should not have
• anything not related

```html
<!DOCTYPE html>
<html lang="en">
<head>
<meta charset="UTF-8">
<title>Cobalt Field Services — Mackay's Sports Turf Specialists</title>
<link href="https://fonts.googleapis.com/css2?family=Montserrat:wght@400;500;600;700;800;900&display=swap" rel="stylesheet">
<style>
:root{
  --bg:#050606;
  --panel:#161b1f;
  --panel-2:#1d2328;
  --strip:#1a2024;
  --green:#3aa935;
  --green-dark:#23801f;
  --blue:#1d8fe1;
  --white:#ffffff;
  --muted:#b9c0c4;
  --line:#2a3136;
}
*{margin:0;padding:0;box-sizing:border-box}
html,body{width:1200px;height:4920px;overflow:hidden}
body{background:var(--bg);color:var(--white);font-family:"Montserrat",Arial,sans-serif;position:relative}
.section{position:absolute;left:0;width:1200px}
.h-display{font-weight:900;text-transform:uppercase;letter-spacing:3px;line-height:1.15}
.btn{display:inline-block;font-weight:800;font-size:13px;letter-spacing:1.5px;text-transform:uppercase;padding:12px 22px;color:var(--white);text-decoration:none}
.btn-green{background:var(--green)}
.btn-blue{background:var(--blue)}
.btn-outline{border:2px solid var(--green);color:var(--green);background:transparent}
.photo{position:absolute}

/* header */
.site-header{top:0;height:80px;z-index:5;display:flex;align-items:center;padding:0 32px}
.brand{font-weight:800;font-size:20px;letter-spacing:1px;color:var(--white);display:flex;align-items:center;gap:10px}
.brand-dot{width:14px;height:14px;border-radius:50%;background:var(--green)}
.main-nav{position:absolute;left:420px;top:30px;display:flex;gap:34px}
.main-nav a{color:var(--white);text-decoration:none;font-weight:700;font-size:14px;letter-spacing:1px;text-transform:uppercase}
.main-nav a.active{color:var(--green);border-bottom:2px solid var(--green);padding-bottom:4px}

/* hero */
.hero{top:0;height:660px;overflow:hidden}
.hero-photo{inset:0;background:
  linear-gradient(90deg,rgba(0,0,0,.72) 0%,rgba(0,0,0,.35) 45%,rgba(0,0,0,0) 70%),
  linear-gradient(180deg,#1c2a18 0%,#2e4a22 30%,#4d7a2e 60%,#6fa23a 100%)}
.hero-copy{position:absolute;left:112px;top:215px;width:720px}
.hero-copy h1{font-size:42px}
.hero-copy p{margin-top:22px;font-size:17px;line-height:1.5;font-weight:500;width:500px}
.hero-actions{margin-top:30px;display:flex;gap:18px}
.slider-arrow{position:absolute;top:350px;width:30px;height:40px}
.slider-arrow.prev{left:14px}
.slider-arrow.next{right:14px}

/* feature strip */
.feature-strip{top:660px;height:240px;background:var(--strip);display:grid;grid-template-columns:repeat(6,1fr);padding:0 90px;align-items:center}
.feature{text-align:center}
.feature svg{width:54px;height:54px;margin:0 auto 16px;display:block}
.feature span{font-size:15px;font-weight:600;line-height:1.35;display:block}

/* about */
.about{top:1020px;height:400px}
.about-photo{left:112px;top:0;width:688px;height:400px;background:linear-gradient(180deg,#f0b46a 0%,#a68a6a 22%,#3f6a2e 45%,#5c8f33 70%,#3d6b24 100%)}
.about-card{position:absolute;left:660px;top:40px;width:428px;height:340px;background:var(--panel);padding:40px 36px;text-align:center}
.about-card h2{color:var(--green);font-size:30px}
.about-card h3{font-weight:800;font-size:18px;letter-spacing:1.5px;margin-top:10px;text-transform:uppercase}
.about-card p{font-size:13px;line-height:1.6;color:var(--muted);margin:16px 0 24px}

/* services */
.services{top:1540px;height:500px;background:var(--panel)}
.services-panel{position:absolute;left:112px;top:0;width:388px;height:500px;background:linear-gradient(180deg,var(--green) 0%,var(--green-dark) 100%);padding:50px 36px}
.services-panel h2{font-size:30px}
.services-panel>p{font-size:13px;line-height:1.55;margin:16px 0 24px}
.service-item{display:flex;gap:14px;align-items:center;margin-bottom:22px}
.service-item .ico{width:42px;height:42px;border-radius:50%;background:rgba(255,255,255,.2);flex:none;display:flex;align-items:center;justify-content:center}
.service-item b{display:block;font-size:14px;font-weight:700}
.service-item small{font-size:12px;color:#e3f3e2}
.supply{position:absolute;left:560px;top:70px;width:530px}
.supply h2{font-size:30px}
.supply p{font-size:14px;line-height:1.55;color:var(--muted);margin-top:16px}
.supply-photo-a{left:560px;top:240px;width:256px;height:240px;background:linear-gradient(180deg,#2c3a44 0%,#4a5e66 40%,#3e7a34 75%,#2e5f25 100%)}
.supply-photo-b{left:844px;top:240px;width:256px;height:240px;background:linear-gradient(180deg,#5b8a3c 0%,#7e6a4a 55%,#3b2c1c 100%)}

/* products */
.section-title{text-align:center;font-size:30px}
.products-title{top:2200px}
.products{top:2280px;left:112px;width:976px;height:380px;background:var(--panel)}
.product-grid{position:absolute;left:40px;top:40px;display:grid;grid-template-columns:repeat(4,200px);gap:32px}
.product{text-align:center}
.product-img{position:relative;width:200px;height:180px;background:#fff;border-radius:60px 0 0 0;padding:14px}
.product-img div{width:100%;height:100%}
.product h4{font-size:15px;font-weight:700;margin-top:16px}
.product .price{font-size:17px;font-weight:700;margin-top:6px}
.product .btn{margin-top:14px;padding:9px 18px}

/* membership */
.membership-title{top:2790px}
.plans{top:2870px;left:140px;width:920px;display:grid;grid-template-columns:repeat(4,212px);gap:24px}
.plan{background:var(--panel);height:310px;text-align:center}
.plan-name{background:var(--panel-2);padding:16px 0;font-weight:800;font-size:15px;letter-spacing:2px;text-transform:uppercase;border-bottom:1px solid var(--line)}
.plan-price{font-size:34px;font-weight:700;margin-top:26px}
.plan-price sup{font-size:16px;vertical-align:super}
.plan-price small{font-size:15px;font-weight:600}
.plan p{font-size:12px;line-height:1.55;color:var(--muted);padding:0 24px;margin:16px 0 26px}

/* testimonials */
.testimonials{top:3300px;height:640px}
.testimonial-photo{inset:0;background:radial-gradient(ellipse at 50% 55%,#6b4a2a 0%,#4a3a20 18%,#2f5a22 40%,#1f3f17 75%,#14290f 100%)}
.testimonial-card{position:absolute;left:300px;top:80px;width:600px;height:480px;background:rgba(22,27,31,.92);text-align:center;padding:36px 60px}
.testimonial-card h2{font-size:30px}
.testimonial-card .quote{margin:22px auto 16px;display:block}
.testimonial-card p{font-size:14px;line-height:1.6;color:var(--muted)}
.testimonial-card .who{font-weight:700;margin-top:18px;font-size:15px}
.testimonial-card .where{font-size:12px;color:var(--muted);margin-top:4px}
.t-arrow{position:absolute;top:300px;width:38px;height:38px;border:2px solid #fff;border-radius:50%;display:flex;align-items:center;justify-content:center}
.t-arrow.prev{left:26px}
.t-arrow.next{right:26px}

/* region */
.region{top:3940px;height:400px;background:#07090a}
.region-copy{position:absolute;left:112px;top:60px;width:500px}
.region-copy h2{font-size:30px}
.region-copy p{font-size:13px;line-height:1.6;color:var(--muted);margin:20px 0 26px;width:440px}
.region-photo{left:640px;top:0;width:380px;height:400px;background:linear-gradient(180deg,#0f1d0c 0%,#1f3a16 55%,#3b6a22 100%)}

/* footer */
.site-footer{top:4340px;height:580px;background:#0f1316}
.footer-brand{position:absolute;left:0;width:1200px;top:70px;text-align:center;font-weight:800;font-size:34px;letter-spacing:1px;display:flex;justify-content:center;align-items:center;gap:14px}
.footer-brand .brand-dot{width:22px;height:22px}
.footer-nav{position:absolute;top:190px;left:0;width:1200px;display:flex;justify-content:center;gap:36px}
.footer-nav a{color:var(--white);text-decoration:none;font-weight:700;font-size:14px;letter-spacing:1px;text-transform:uppercase}
.footer-rule{position:absolute;left:112px;width:976px;height:1px;background:var(--line)}
.contact-row{position:absolute;top:270px;left:180px;width:880px;display:grid;grid-template-columns:repeat(3,1fr)}
.contact{display:flex;gap:16px;align-items:flex-start}
.contact .ico{width:48px;height:48px;border-radius:50%;background:var(--green);flex:none;display:flex;align-items:center;justify-content:center}
.contact b{display:block;font-size:14px;font-weight:700;letter-spacing:1px}
.contact span{font-size:13px;color:var(--muted);line-height:1.5}
.copyright{position:absolute;left:180px;top:490px;font-size:13px;color:var(--muted)}
.socials{position:absolute;right:140px;top:480px;display:flex;gap:10px}
.socials i{width:32px;height:32px;border-radius:50%;background:var(--green);display:block}
</style>
</head>
<body>

<header class="section site-header">
  <div class="brand"><span class="brand-dot"></span>Cobalt Field Services</div>
  <nav class="main-nav">
    <a class="active" href="#">Home</a>
    <a href="#">Shop</a>
    <a href="#">Gallery</a>
    <a href="#">Grants Initiative</a>
    <a href="#">Northreach Finest Green</a>
  </nav>
</header>

<section class="section hero">
  <div class="photo hero-photo" role="img" aria-label="Groundskeeper mowing a sports field on a ride-on mower with trees behind"></div>
  <div class="hero-copy">
    <h1 class="h-display">CFS Mackay's Sports<br>Turf Specialists</h1>
    <p>From elite sports fields to community parks, we deliver premium turf management, maintenance, and supply solutions across the Mackay region.</p>
    <div class="hero-actions">
      <a class="btn btn-green" href="#">Get a Turf Quote</a>
      <a class="btn btn-blue" href="#">View Our Work</a>
    </div>
  </div>
  <svg class="slider-arrow prev" viewBox="0 0 30 40"><path d="M22 4 8 20l14 16" fill="none" stroke="#fff" stroke-width="4"/></svg>
  <svg class="slider-arrow next" viewBox="0 0 30 40"><path d="M8 4l14 16L8 36" fill="none" stroke="#fff" stroke-width="4"/></svg>
</section>

<section class="section feature-strip">
  <div class="feature">
    <svg viewBox="0 0 54 54" fill="none" stroke="#fff" stroke-width="2.5"><circle cx="18" cy="18" r="7"/><circle cx="36" cy="18" r="7"/><path d="M6 44c0-9 6-14 12-14s12 5 12 14M24 44c0-9 6-14 12-14s12 5 12 14"/></svg>
    <span>Sporting<br>Associations</span>
  </div>
  <div class="feature">
    <svg viewBox="0 0 54 54" fill="none" stroke="#fff" stroke-width="2.5"><path d="M6 46h42M10 46V22l17-12 17 12v24M20 46V32h14v14"/></svg>
    <span>Community<br>Facilities</span>
  </div>
  <div class="feature">
    <svg viewBox="0 0 54 54" fill="none" stroke="#fff" stroke-width="2.5"><path d="M6 44h42M12 44c0-10 3-18 6-22M22 44c0-12 3-22 5-28M32 44c0-12-2-22-4-28M42 44c0-10-3-18-6-22"/></svg>
    <span>Sports<br>Turf</span>
  </div>
  <div class="feature">
    <svg viewBox="0 0 54 54" fill="none" stroke="#fff" stroke-width="2.5"><path d="M27 48s-15-15-15-27a15 15 0 0 1 30 0c0 12-15 27-15 27z"/><circle cx="27" cy="21" r="6"/></svg>
    <span>Mackay Region<br>Soccer</span>
  </div>
  <div class="feature">
    <svg viewBox="0 0 54 54" fill="none" stroke="#fff" stroke-width="2.5"><circle cx="27" cy="27" r="18"/><path d="M14 14c6 6 6 20 0 26M40 14c-6 6-6 20 0 26"/></svg>
    <span>Softball<br>Fields</span>
  </div>
  <div class="feature">
    <svg viewBox="0 0 54 54" fill="none" stroke="#fff" stroke-width="2.5"><path d="M8 34h30l6-10h4M12 34v6M36 34v6"/><circle cx="14" cy="42" r="4"/><circle cx="36" cy="42" r="4"/><path d="M18 34V20h12v14"/></svg>
    <span>Turf Management<br>Products</span>
  </div>
</section>

<section class="section about">
  <div class="photo about-photo" role="img" aria-label="Aerial view of a softball diamond at sunset"></div>
  <div class="about-card">
    <h2 class="h-display">About Us</h2>
    <h3>Your Turf. Our Passion.</h3>
    <p>At Cobalt Field Services, we're dedicated to growing, maintaining, and managing world-class sports surfaces. Whether it's a soccer pitch, rugby field, or softball diamond, we tailor complete turf management programs to suit your needs — from full maintenance contracts to one-off supply and apply services.</p>
    <a class="btn btn-green" href="#">View Our Work</a>
  </div>
</section>

<section class="section services">
  <div class="services-panel">
    <h2 class="h-display">Our Services</h2>
    <p>Through our Cobalt Grants Initiative, we help clubs and councils secure funding opportunities to improve and maintain turf facilities.</p>
    <div class="service-item"><div class="ico"><svg width="20" height="20" viewBox="0 0 20 20"><path d="M3 10l5 5 9-10" fill="none" stroke="#fff" stroke-width="2.5"/></svg></div><div><b>Complete Turf Management Plans</b><small>Seasonal and year-round programs</small></div></div>
    <div class="service-item"><div class="ico"><svg width="20" height="20" viewBox="0 0 20 20"><path d="M3 10l5 5 9-10" fill="none" stroke="#fff" stroke-width="2.5"/></svg></div><div><b>Fertiliser &amp; Product Supply</b><small>Professional-grade turf care products</small></div></div>
    <div class="service-item"><div class="ico"><svg width="20" height="20" viewBox="0 0 20 20"><path d="M3 10l5 5 9-10" fill="none" stroke="#fff" stroke-width="2.5"/></svg></div><div><b>Supply &amp; Apply Services</b><small>Expert application for consistent results</small></div></div>
    <div class="service-item"><div class="ico"><svg width="20" height="20" viewBox="0 0 20 20"><path d="M3 10l5 5 9-10" fill="none" stroke="#fff" stroke-width="2.5"/></svg></div><div><b>Grounds &amp; Facility Maintenance</b><small>High-standard care for premium sites</small></div></div>
  </div>
  <div class="supply">
    <h2 class="h-display">Fertiliser &amp; Product<br>Supply</h2>
    <p>At Cobalt Field Services, we're dedicated to growing, maintaining, and managing world-class sports surfaces.</p>
  </div>
  <div class="photo supply-photo-a" role="img" aria-label="Indoor sports field under floodlights"></div>
  <div class="photo supply-photo-b" role="img" aria-label="Bag of fertiliser on turf with soil"></div>
</section>

<h2 class="section section-title h-display products-title">Featured Products</h2>
<section class="section products">
  <div class="product-grid">
    <div class="product">
      <div class="product-img"><div role="img" aria-label="Square of seed and turf repair grass" style="background:linear-gradient(135deg,#5fae3a,#2f7a22)"></div></div>
      <h4>Seed &amp; Turf Repair</h4><div class="price">$45.00</div><a class="btn btn-green" href="#">Shop Now</a>
    </div>
    <div class="product">
      <div class="product-img"><div role="img" aria-label="Square of dark nutrient-rich soil" style="background:linear-gradient(135deg,#3a2a1c,#1e140c)"></div></div>
      <h4>Nutrients &amp; Fertilisers</h4><div class="price">$45.00</div><a class="btn btn-green" href="#">Shop Now</a>
    </div>
    <div class="product">
      <div class="product-img"><div role="img" aria-label="Sacks of soil conditioner" style="background:linear-gradient(135deg,#c9a77c,#7a5a3a)"></div></div>
      <h4>Soil Conditioners</h4><div class="price">$45.00</div><a class="btn btn-green" href="#">Shop Now</a>
    </div>
    <div class="product">
      <div class="product-img"><div role="img" aria-label="Square of turf repair grass" style="background:linear-gradient(135deg,#6ab83e,#347f25)"></div></div>
      <h4>Seed &amp; Turf Repair</h4><div class="price">$45.00</div><a class="btn btn-green" href="#">Shop Now</a>
    </div>
  </div>
</section>

<h2 class="section section-title h-display membership-title">Club Membership</h2>
<section class="section plans">
  <div class="plan"><div class="plan-name">Junior</div><div class="plan-price"><sup>$</sup>250 <small>/Mt</small></div><p>Seasonal field access, priority bookings and turf care tips for members.</p><a class="btn btn-outline" href="#">Order Now</a></div>
  <div class="plan"><div class="plan-name">Individual</div><div class="plan-price"><sup>$</sup>150 <small>/Mt</small></div><p>Seasonal field access, priority bookings and turf care tips for members.</p><a class="btn btn-outline" href="#">Order Now</a></div>
  <div class="plan"><div class="plan-name">Friends</div><div class="plan-price"><sup>$</sup>350 <small>/Mt</small></div><p>Seasonal field access, priority bookings and turf care tips for members.</p><a class="btn btn-outline" href="#">Order Now</a></div>
  <div class="plan"><div class="plan-name">Family</div><div class="plan-price"><sup>$</sup>450 <small>/Mt</small></div><p>Seasonal field access, priority bookings and turf care tips for members.</p><a class="btn btn-outline" href="#">Order Now</a></div>
</section>

<section class="section testimonials">
  <div class="photo testimonial-photo" role="img" aria-label="Softball glove and ball resting on green grass"></div>
  <div class="testimonial-card">
    <h2 class="h-display">Testimonials</h2>
    <svg class="quote" width="60" height="44" viewBox="0 0 60 44"><path d="M4 40V22C4 10 10 4 22 2v8c-6 2-8 6-8 12h8v18zM34 40V22c0-12 6-18 18-20v8c-6 2-8 6-8 12h8v18z" fill="none" stroke="#fff" stroke-width="2.5"/></svg>
    <p>Our fields have never looked better. The team arrived on schedule, explained every step of the program and left the surface in match-ready condition. Players and parents have noticed the difference all season, and our committee now plans every upgrade with them.</p>
    <div class="who">-Mara Ellison</div>
    <div class="where">United State</div>
  </div>
  <div class="t-arrow prev"><svg width="14" height="14" viewBox="0 0 14 14"><path d="M9 2 4 7l5 5" fill="none" stroke="#fff" stroke-width="2.5"/></svg></div>
  <div class="t-arrow next"><svg width="14" height="14" viewBox="0 0 14 14"><path d="M5 2l5 5-5 5" fill="none" stroke="#fff" stroke-width="2.5"/></svg></div>
</section>

<section class="section region">
  <div class="region-copy">
    <h2 class="h-display">Mackay Region<br>Soccer Rugby League<br>Softball Fields</h2>
    <p>We look after match grounds across the region, keeping every pitch safe, even and ready for play. From preseason renovation to weekly mowing, our crews tailor each program to the sport, the soil and the season, so clubs can focus on the game.</p>
    <a class="btn btn-green" href="#">View Our Work</a>
  </div>
  <div class="photo region-photo" role="img" aria-label="Decorative graphic of a softball lying on grass"></div>
</section>

<footer class="section site-footer">
  <div class="footer-brand"><span class="brand-dot"></span>Cobalt Field Services</div>
  <nav class="footer-nav">
    <a href="#">Home</a><a href="#">Grants Initiative</a><a href="#">Shop</a><a href="#">Gallery</a><a href="#">Contact Us</a><a href="#">Northreach Finest Green</a>
  </nav>
  <div class="footer-rule" style="top:240px"></div>
  <div class="contact-row">
    <div class="contact"><div class="ico"><svg width="22" height="22" viewBox="0 0 24 24"><path d="M6 3h4l2 5-3 2a11 11 0 0 0 5 5l2-3 5 2v4a2 2 0 0 1-2 2A17 17 0 0 1 4 5a2 2 0 0 1 2-2z" fill="#fff"/></svg></div><div><b>PHONE:</b><span>+61 7 4951 2200</span></div></div>
    <div class="contact"><div class="ico"><svg width="22" height="22" viewBox="0 0 24 24"><rect x="3" y="5" width="18" height="14" rx="2" fill="none" stroke="#fff" stroke-width="2"/><path d="m3 7 9 6 9-6" fill="none" stroke="#fff" stroke-width="2"/></svg></div><div><b>E-MAIL:</b><span>hello@cobaltfield.com.au</span></div></div>
    <div class="contact"><div class="ico"><svg width="22" height="22" viewBox="0 0 24 24"><path d="M12 22s-7-7-7-12a7 7 0 0 1 14 0c0 5-7 12-7 12z" fill="#fff"/><circle cx="12" cy="10" r="2.5" fill="#3aa935"/></svg></div><div><b>ADDRESS:</b><span>14 Harbour Road Mackay<br>QLD 4740 Australia</span></div></div>
  </div>
  <div class="footer-rule" style="top:450px"></div>
  <div class="copyright">Copyright © 2025 Cobalt Field Services All Rights Reserved</div>
  <div class="socials"><i></i><i></i><i></i><i></i><i></i></div>
</footer>

</body>
</html>
```